Website for a company offering full serivce charging solutions for electric cars

The company "vorn-werk" (english: "front-works") offering all-in-one-solutions for charging infrastructure for electric mobility.

There are four products:
1- Wallboxes for single-family homes
2- Solutions for property devloper/-management for property parking space
3- All-in-one-charging solution for municipalities/communities
4- Solutions for tourism/hotels/holiday appartments

The Website structure:
1. Main Page
2.1. Product Page Single Homes
2.2. Product Page Property Management / Parking
2.3. Product Page Municipality
2.4. Product Page Tourism
3. Contact Form / Request for information
4. Imprint / Legal

The Website should be built on Wordpress with a powerful possibility to simply add/modify specific landing pages.

We would like you to implement the website later and also maintain it if possible, but we would be able to do minor modifications by ourselfs (for A/B-Testing)

The website should be clear and simple, easy to understand.
Target group is mainly B2C without deeper knowledge of that topic.

It should suggest, that we will provide a very simple way to get the charging infrastructure done.

We need a contact form, maybe we will use Leadmill later.

Attached you will find a draft of the main page and a landing page (for 2.2) - it is just the content, please ignore the design. We would love to let you create a suitable design.
Also you will find some drafts a bit different for the same story.

I added also a few stock photos, but they don't need to be used! If you have better ideas, you are welcome!

Charging/Electric mobility

Sans Serif

• Based on Wordpress, and the designer should be able to implement it on Wordpress on a later step

```html
<!DOCTYPE html>
<html lang="de">
<head>
<meta charset="utf-8">
<title>vorn-werk.de – Ladelösungen</title>
<link rel="stylesheet" href="https://fonts.googleapis.com/css2?family=Exo+2:wght@400;500;600;700&family=Mulish:wght@400;500;600;700&display=swap">
<style>
:root{
  --navy:#131a2e;
  --navy-deep:#0e1426;
  --navy-light:#0f1f3f;
  --pink:#e5168c;
  --violet:#8a3fd6;
  --white:#ffffff;
  --muted:#b9bfd1;
  --line:#3a2a5c;
  --btn:linear-gradient(90deg,#8b45e0 0%,#e0189a 100%);
}
*{box-sizing:border-box;margin:0;padding:0}
html,body{width:1200px;height:4244px;overflow:hidden}
body{background:var(--navy);color:var(--white);font-family:"Mulish",sans-serif;position:relative}
.abs{position:absolute}
.heading{font-family:"Exo 2",sans-serif}
.btn{position:absolute;display:flex;align-items:center;justify-content:center;border-radius:30px;background:var(--btn);font-family:"Exo 2",sans-serif;font-weight:700;font-size:19px;color:var(--white);letter-spacing:.5px;box-shadow:0 6px 18px rgba(160,40,200,.35)}
/* header */
.site-header{top:0;left:0;width:1200px;height:80px;background:var(--navy-deep);border-bottom:2px solid var(--violet)}
.brand{left:104px;top:18px;display:flex;align-items:center;gap:12px}
.brand-dot{width:42px;height:42px;border-radius:50%;border:3px solid var(--pink)}
.brand-name{font-family:"Exo 2",sans-serif;font-size:26px;font-weight:500;line-height:1}
.brand-tag{font-size:13px;color:var(--muted);margin-top:3px}
.nav-link{top:32px;font-size:16px;color:var(--white)}
.nav-link.active{border-bottom:2px solid var(--pink);padding-bottom:8px}
/* hero */
.hero{top:80px;left:0;width:1200px;height:596px;background:radial-gradient(circle at 78% 45%,#3a5aa8 0%,#222c4e 30%,#1a1e34 60%,#121624 100%)}
.hero-title{left:110px;top:240px;font-size:54px;line-height:54px;font-weight:700;white-space:nowrap}
.hero-title span{font-weight:400;display:block}
.hero-sub{left:110px;top:362px;font-size:20px;line-height:30px;white-space:nowrap}
.arrow{top:350px}
/* intro */
.intro-lead{left:170px;width:860px;top:805px;text-align:center;font-size:22px;line-height:33px;font-weight:600}
.intro-text{left:190px;width:820px;top:920px;text-align:center;font-size:16px;line-height:27.5px;color:var(--muted)}
.grid-band{left:0;width:1200px;background:linear-gradient(180deg,rgba(229,22,140,0) 0%,rgba(138,63,214,.18) 60%,rgba(229,22,140,.08) 100%)}
.section-title{font-size:37px;font-weight:500;text-align:center;width:1200px;left:0}
.card{top:1325px;width:307px;height:178px;border-radius:6px;background:linear-gradient(180deg,#2b3e62 0%,#1a2846 70%,#253552 100%);box-shadow:0 0 20px rgba(40,80,160,.35)}
.card-dots{top:1390px;width:300px;height:122px;border-left:3px dotted var(--pink);border-bottom:3px dotted var(--pink)}
.card-label{top:1418px;width:307px;text-align:center;font-family:"Exo 2",sans-serif;font-size:22px;font-weight:600;white-space:nowrap}
.card-icon{top:1370px}
.card-chev{top:1464px}
/* product sections */
.photo{position:absolute}
.product-title{font-family:"Exo 2",sans-serif;color:var(--pink);font-size:38px;font-weight:600}
.list{position:absolute;list-style:none;font-size:13.5px;line-height:17px}
.list li{position:relative;padding-left:16px;margin-bottom:9px}
.list li::before{content:"";position:absolute;left:0;top:4px;width:6px;height:6px;border-top:2px solid var(--pink);border-right:2px solid var(--pink);transform:rotate(45deg)}
.list ul{list-style:none;margin-top:6px}
.list ul li{margin-bottom:2px}
.section-alt{top:2134px;left:0;width:1200px;height:684px;background:var(--navy-light)}
/* contact */
.contact{top:3349px;left:0;width:1200px;height:532px;background:linear-gradient(100deg,#d21aa8 0%,#a22ac4 35%,#5a3fd0 65%,#3250b8 100%)}
.contact-photo{left:640px;top:3349px;width:560px;height:532px;background:linear-gradient(100deg,rgba(180,160,230,0) 0%,rgba(200,190,240,.35) 45%,rgba(70,90,190,.5) 100%)}
.contact-title{left:110px;top:3410px;font-size:40px;font-weight:500}
.contact-title b{font-weight:700}
.contact-text{left:114px;top:3474px;width:470px;font-size:15px;line-height:19px}
.field{position:absolute;background:var(--white);color:#555;font-size:12px;padding:14px 16px;border:1px solid #ddd}
.submit{position:absolute;left:110px;top:3751px;width:177px;height:46px;border:2px solid var(--white);border-radius:25px;display:flex;align-items:center;justify-content:center;font-family:"Exo 2",sans-serif;font-weight:700;font-size:17px}
/* footer */
.footer{top:3881px;left:0;width:1200px;height:297px;background:var(--navy-deep)}
.footer-divider{top:3881px;width:1px;height:297px;background:#252c44}
.footer-head{top:3952px;font-family:"Exo 2",sans-serif;font-weight:700;font-size:18px;padding-left:22px;border-left:3px solid var(--pink);line-height:22px}
.footer-link{font-size:15px;color:var(--muted)}
.social{top:3993px;width:34px;height:34px;border-radius:50%;background:var(--pink)}
.bottom-bar{top:4178px;left:0;width:1200px;height:66px;background:#202538;text-align:center;font-size:14px;line-height:66px;color:var(--muted)}
</style>
</head>
<body>

<header class="abs site-header">
  <div class="abs brand">
    <span class="brand-dot"></span>
    <div><div class="brand-name">vorn-werk.de</div><div class="brand-tag">einfach mehr als laden</div></div>
  </div>
  <a class="abs nav-link active" style="left:456px">Lösungen</a>
  <a class="abs nav-link" style="left:585px">Unternehmen</a>
  <a class="abs nav-link" style="left:745px">Services</a>
  <a class="abs nav-link" style="left:864px">Karriere</a>
  <a class="btn" style="left:966px;top:23px;width:125px;height:40px;font-size:16px;font-family:'Mulish',sans-serif">Kontakt</a>
</header>

<section class="abs hero" role="img" aria-label="Nahaufnahme eines Ladesteckers an einer Ladesäule bei Nacht"></section>
<h1 class="abs heading hero-title">VORN-WERK IST<span>IHR PARTNER</span></h1>
<p class="abs hero-sub">wenn das Laden nicht nur einfach, sondern die<br>Umsetzung auch aus einer Hand kommen soll</p>
<a class="btn" style="left:112px;top:438px;width:171px;height:53px">KONTAKT</a>
<svg class="abs arrow" style="left:24px" width="20" height="28" viewBox="0 0 20 28"><path d="M15 3 L5 14 L15 25" fill="none" stroke="#fff" stroke-width="3"/></svg>
<svg class="abs arrow" style="left:1158px" width="20" height="28" viewBox="0 0 20 28"><path d="M5 3 L15 14 L5 25" fill="none" stroke="#fff" stroke-width="3"/></svg>

<p class="abs intro-lead">Wir &nbsp;bieten Lösungen sowohl für Privatkunden, Geschäftskunden als auch Kommunen an, die schnell, fair und ohne Eigenleistung zu einer smarten Ladelösung für E-Fahrzeuge kommen möchten.</p>
<p class="abs intro-text">Von der Beratung, über die Installation, Inbetriebnahme bis zur Abrechnung und Wartung bekommen Sie bei vorn-werk alles aus einer Hand. Auf Wunsch vermieten wir auch die Ladetechnik und übernehmen im gewerblichen Bereich die direkte Abrechnung mit dem Nutzer. Für Kommunen bieten wir den kostenfreien Full-Service an und beteiligen die Gemeinden an der Nutzung der Infrastruktur.</p>
<div class="abs grid-band" style="top:1055px;height:132px" role="img" aria-label="Leuchtender Perspektiv-Raster als Hintergrund"></div>

<h2 class="abs heading section-title" style="top:1230px">Ladelösung für</h2>

<div class="abs card-dots" style="left:112px"></div>
<div class="abs card-dots" style="left:444px"></div>
<div class="abs card-dots" style="left:777px"></div>
<div class="abs card" style="left:124px" role="img" aria-label="Wallbox am Einfamilienhaus"></div>
<div class="abs card" style="left:456px" role="img" aria-label="Ladeplätze in einer Wohnanlage"></div>
<div class="abs card" style="left:789px" role="img" aria-label="Öffentliche Ladesäule in der Gemeinde"></div>

<svg class="abs card-icon" style="left:256px" width="42" height="42" viewBox="0 0 42 42" fill="none" stroke="#fff" stroke-width="2"><path d="M4 20 L21 5 L38 20"/><path d="M9 16 V38 H33 V16"/><path d="M17 38 V26 H25 V38"/></svg>
<svg class="abs card-icon" style="left:587px;top:1362px" width="50" height="50" viewBox="0 0 50 50" fill="none" stroke="#fff" stroke-width="2"><rect x="16" y="4" width="16" height="42"/><rect x="4" y="20" width="12" height="26"/><rect x="32" y="16" width="14" height="30"/><path d="M20 10h8M20 16h8M20 22h8M20 28h8M8 26h4M8 32h4M36 22h6M36 28h6"/></svg>
<svg class="abs card-icon" style="left:917px;top:1362px" width="52" height="52" viewBox="0 0 52 52" fill="none" stroke="#fff" stroke-width="2"><circle cx="26" cy="26" r="23" stroke-dasharray="8 4"/><circle cx="26" cy="20" r="5"/><path d="M17 36c2-6 16-6 18 0"/><circle cx="15" cy="24" r="3"/><circle cx="37" cy="24" r="3"/></svg>

<div class="abs card-label" style="left:124px">Eigenheimbesitzer</div>
<div class="abs card-label" style="left:456px;top:1420px">Hausverwaltung/Bauträger</div>
<div class="abs card-label" style="left:789px;top:1420px">Gemeinden/Kommunen</div>
<svg class="abs card-chev" style="left:271px" width="14" height="16" viewBox="0 0 14 16" fill="none" stroke="#fff" stroke-width="2"><path d="M2 2l5 5 5-5M2 8l5 5 5-5"/></svg>
<svg class="abs card-chev" style="left:603px" width="14" height="16" viewBox="0 0 14 16" fill="none" stroke="#fff" stroke-width="2"><path d="M2 2l5 5 5-5M2 8l5 5 5-5"/></svg>
<svg class="abs card-chev" style="left:936px" width="14" height="16" viewBox="0 0 14 16" fill="none" stroke="#fff" stroke-width="2"><path d="M2 2l5 5 5-5M2 8l5 5 5-5"/></svg>

<!-- Eigenheimbesitzer -->
<div class="photo" style="left:109px;top:1635px;width:460px;height:359px;border-radius:60px 0 60px 0;background:linear-gradient(120deg,#d9d4cc 0%,#a89f95 45%,#4a4540 100%)" role="img" aria-label="Frau lädt ihr E-Auto an der Wallbox zu Hause"></div>
<h2 class="abs product-title" style="left:621px;top:1638px">Eigenheimbesitzer</h2>
<ul class="list" style="left:622px;top:1719px;width:520px">
  <li>Bestandsanalyse mit umfangreicher Beratung über die Möglichkeiten der Umsetzung</li>
  <li>Prüfung und Übernahme der Anmeldung verfügbarer Fördermöglichkeiten</li>
  <li>Auswahl an smarten Wallbox Lösungen, passend für Ihr Fahrzeug und Ihre Bedürfnisse</li>
  <li>Installation inkl. aller notwendigen Materialien und Tätigkeiten (Durchbrüche, Erdarbeiten, etc.)</li>
  <li>Inbetriebnahme und Einweisung in die Ladetechnik</li>
  <li>Jährlich technische Wartung nach DGUV3</li>
</ul>
<a class="btn" style="left:621px;top:1938px;width:173px;height:53px">MEHR</a>
<div class="abs grid-band" style="top:1994px;height:140px" role="img" aria-label="Leuchtender Perspektiv-Raster als Hintergrund"></div>

<!-- Hausverwaltung -->
<div class="abs section-alt"></div>
<h2 class="abs product-title" style="left:0;width:1145px;text-align:center;top:2176px">Hausverwaltung / Bauträger</h2>
<ul class="list" style="left:132px;top:2295px;width:470px">
  <li>Durchführung einer individuellen Bedarfsanalyse inkl. Ermittlung der Anforderungen für:
    <ul>
      <li>Haus- und Immobilienverwaltungen</li>
      <li>Dienstleistungs- und Handelsunternehmen</li>
      <li>Hotel und Beherbergungsbetriebe</li>
      <li>Parkraum- und Parkhausbetreiber</li>
      <li>Tourismus, Sport- und Freizeiteinrichtungen</li>
    </ul>
  </li>
  <li style="margin-top:22px">Planung und Projektierung des Installationsaufwands inkl.</li>
  <li>Materialverbrauch</li>
  <li>Leasing oder Kauf der Hardware</li>
</ul>
<ul class="list" style="left:628px;top:2284px;width:470px">
  <li>Bei Bestandsbauten Integration der Ladeinfrastruktur in die</li>
  <li>Gebäudesystemtechnik und ggf. Anpassung des Netzanschlusses</li>
  <li>Inbetriebnahme der Anlage inkl. Prüf- und Messprotokollen</li>
  <li>Wiederkehrende technische Prüfung der Anlage nach DGUV 3</li>
  <li>Austausch und Reparatur Service</li>
</ul>
<a class="btn" style="left:124px;top:2563px;width:173px;height:53px">MEHR</a>
<div class="photo" style="left:613px;top:2444px;width:430px;height:311px;border-radius:0 0 60px 0;background:linear-gradient(160deg,#8f9296 0%,#5c5f63 45%,#2a2c30 100%)" role="img" aria-label="Dunkler SUV in einer Tiefgarage mit Ladestation"></div>
<div class="abs grid-band" style="top:2680px;height:138px" role="img" aria-label="Leuchtender Perspektiv-Raster als Hintergrund"></div>

<!-- Kommune -->
<div class="photo" style="left:137px;top:2930px;width:428px;height:313px;border-radius:60px 0 60px 0;background:linear-gradient(135deg,#f0b34a 0%,#b57a3a 40%,#4a3a2e 100%)" role="img" aria-label="Frau mit Smartphone lädt ihr E-Auto bei Sonnenuntergang"></div>
<h2 class="abs product-title" style="left:623px;top:2926px">Kommune /Gemeinde</h2>
<ul class="list" style="left:623px;top:2986px;width:470px">
  <li style="margin-bottom:2px">&nbsp;</li>
  <li>Regelmäßige Wartung gemäß Vorschrift</li>
  <li style="padding-left:20px">Reparatur und Kundenservice</li>
  <li>Direkte Abrechnung mit dem Nutzer</li>
  <li>Beteiligung der Gemeinde am Umsatz</li>
  <li>Möglichkeit der Integration von Bonusprogrammen, mit denen der lokale Einzelhandel beworben wird</li>
</ul>
<a class="btn" style="left:613px;top:3176px;width:173px;height:53px">MEHR</a>
<div class="abs grid-band" style="top:3240px;height:109px" role="img" aria-label="Leuchtender Perspektiv-Raster als Hintergrund"></div>

<!-- Contact -->
<section class="abs contact"></section>
<div class="abs contact-photo" role="img" aria-label="Weißes E-Auto lädt an einer Wandladestation"></div>
<h2 class="abs heading contact-title"><b>CONTACT</b> US</h2>
<p class="abs contact-text">Lorem ipsum dolor sit amet, consectetur adipiscing elit, sed do eiusmod tempor incididunt ut labore et dolore magna aliqua.</p>
<div class="field" style="left:114px;top:3541px;width:237px;height:43px">First Name</div>
<div class="field" style="left:358px;top:3541px;width:237px;height:43px">Last Name</div>
<div class="field" style="left:114px;top:3594px;width:237px;height:43px">Email address</div>
<div class="field" style="left:358px;top:3594px;width:237px;height:43px">Phone number</div>
<div class="field" style="left:114px;top:3647px;width:481px;height:91px">Message</div>
<div class="submit">SUBMIT NOW</div>

<!-- Footer -->
<footer class="abs footer"></footer>
<div class="abs" style="left:109px;top:3960px;display:flex;align-items:center;gap:14px">
  <span style="width:34px;height:34px;border-radius:50%;border:3px solid var(--pink)"></span>
  <span style="font-family:'Exo 2',sans-serif;font-size:36px;font-weight:500">vorn-werk.de</span>
</div>
<div class="abs footer-divider" style="left:392px"></div>
<div class="abs footer-divider" style="left:651px"></div>
<div class="abs footer-divider" style="left:867px"></div>
<div class="abs footer-head" style="left:392px">NAVIGATION</div>
<div class="abs footer-head" style="left:651px">RESOURCES</div>
<div class="abs footer-head" style="left:864px">FOLLOW US</div>
<a class="abs footer-link" style="left:418px;top:3990px">AGB</a>
<a class="abs footer-link" style="left:418px;top:4021px">Datenschutzerklärung</a>
<a class="abs footer-link" style="left:418px;top:4053px">Impressum</a>
<a class="abs footer-link" style="left:674px;top:3990px">Kontakt</a>
<a class="abs footer-link" style="left:674px;top:4021px">Karriere</a>
<a class="abs footer-link" style="left:674px;top:4053px">FAQs</a>
<span class="abs social" style="left:883px" aria-label="Soziales Netzwerk 1"></span>
<span class="abs social" style="left:924px" aria-label="Soziales Netzwerk 2"></span>
<span class="abs social" style="left:965px" aria-label="Soziales Netzwerk 3"></span>
<span class="abs social" style="left:1006px" aria-label="Soziales Netzwerk 4"></span>
<div class="abs bottom-bar">© 2022 vorn-werk GmbH</div>

</body>
</html>
```